Use your magic to make a startup company look established*

We are in need of a website that gives the appearance that we are established rather than new. Our audience is comprised of senior executives in technology professional services companies, financial people (conservative) that invest in them, and executives in companies that are in need of their services. The site therefore needs to lean towards the conservative side while being modern and professional.

This should be a fairly simple site.

- About us
- Services
- Contacts
- Content (Articles)

It should be SEO friendly and easy to add content or sub pages. A responsive design is mandatory.

Target Market(s)

We work with executives and investors in professional services companies to more effectively compete in the already crowded “digital transformation” market.

Industry/Entity Type

Professional Service

Coding

Coded - Design and coding required

Number of Pages Required

5+ page

Font styles to use
Sans Serif

Requirements
Must have
• - Responsive design
- Easy to add/change content
- Easy to add additional pages

```html
<!DOCTYPE html>
<html lang="en">
<head>
<meta charset="utf-8">
<title>Summit Crest Advisors</title>
<link href="https://fonts.googleapis.com/css2?family=Lato:wght@400;700;900&family=Montserrat:wght@600;700&display=swap" rel="stylesheet">
<style>
:root{
  --gold:#c3902f;
  --gold-light:#d9ae45;
  --gold-dark:#b27f25;
  --ink:#111;
  --text:#555;
  --nav:#4a4a4a;
  --soft:#f4f3f3;
  --footer:#1f1f1f;
  --footer-bar:#3b3b3d;
  --white:#fff;
}
*{margin:0;padding:0;box-sizing:border-box}
html,body{width:1200px;height:2278px;overflow:hidden}
body{font-family:'Lato',sans-serif;color:var(--text);background:var(--white);position:relative}
.abs{position:absolute}
a{color:inherit;text-decoration:none}

/* header */
.site-header{position:absolute;top:0;left:0;width:1200px;height:123px;background:var(--white)}
.brand{display:flex;align-items:center;gap:10px;white-space:nowrap}
.brand-dot{width:14px;height:14px;border-radius:50%;background:var(--gold);flex:none}
.brand-name{font-size:19px;font-weight:700;color:#666}
.header-brand{left:122px;top:50px}
.contact-block{font-size:13px}
.contact-block .label{color:var(--gold);font-weight:700;display:flex;align-items:center;gap:6px;text-decoration:underline}
.contact-block .value{color:#333;margin-top:2px;padding-left:18px}
.call{left:415px;top:54px}
.call .value{font-weight:700;font-size:14px}
.mail{left:645px;top:54px}
.mail .value{padding-left:22px;font-size:12.5px}
.follow{left:969px;top:50px}
.follow .label{color:var(--gold);font-weight:700;font-size:13px}
.social-row{display:flex;gap:2px;margin-top:6px}
.social-row span{width:19px;height:18px;background:#555}

/* nav */
.main-nav{position:absolute;top:123px;left:0;width:1200px;height:35px;background:var(--nav)}
.main-nav a{position:absolute;top:0;line-height:35px;font-size:12.5px;font-weight:700;color:var(--white);text-transform:uppercase}
.main-nav a.active{color:var(--gold-light)}
.main-nav a.appointment{left:968px;width:165px;text-align:center;background:linear-gradient(var(--gold-light),var(--gold-dark))}

/* hero */
.hero{position:absolute;top:158px;left:0;width:1200px;height:511px;background:linear-gradient(100deg,#3a3f47 0%,#55595f 30%,#6a6b6d 50%,#4a4d52 70%,#2e3238 100%)}
.hero h1{position:absolute;left:111px;top:240px;font-family:'Montserrat',sans-serif;font-weight:700;font-size:34px;line-height:33px;color:var(--white);width:520px}
.hero p{position:absolute;left:112px;top:352px;font-size:12.5px;line-height:16px;font-weight:700;color:var(--gold);width:440px}
.hero .btn{position:absolute;left:115px;top:402px;width:147px;height:42px;line-height:42px;text-align:center;color:var(--white);font-weight:700;font-size:14px;background:linear-gradient(var(--gold-light),var(--gold-dark))}

/* section heads */
.eyebrow{font-size:13px;color:var(--gold);text-transform:uppercase;text-align:center}
.title{font-size:32px;font-weight:700;color:var(--ink);text-align:center;line-height:38px}

.about{position:absolute;top:669px;left:0;width:1200px;height:362px}
.about .eyebrow{position:absolute;top:50px;width:1194px}
.about .title{position:absolute;top:68px;width:1194px}
.about .copy{position:absolute;left:127px;top:143px;width:940px;font-size:12.5px;line-height:15.3px}
.about .copy p+p{margin-top:16px}
.pill{position:absolute;left:542px;top:275px;width:108px;height:35px;border-radius:18px;line-height:35px;text-align:center;color:var(--white);font-size:9.5px;font-weight:900;letter-spacing:1px;background:linear-gradient(var(--gold-light),var(--gold-dark))}

.services{position:absolute;top:1031px;left:0;width:1200px;height:492px;background:var(--soft)}
.services .eyebrow{position:absolute;top:66px;width:1210px}
.services .title{position:absolute;top:82px;width:1210px}
.services .intro{position:absolute;left:137px;top:143px;width:942px;text-align:center;font-size:12.5px;line-height:20px}
.service{position:absolute;top:224px;width:280px;text-align:center}
.service svg{height:62px;display:block;margin:0 auto}
.service h3{margin-top:20px;font-size:14.5px;font-weight:900;color:var(--ink);text-transform:uppercase}
.service p{margin-top:14px;font-size:12.5px;line-height:15.5px;padding:0 12px}
.service .more{display:block;margin-top:20px;font-size:9.5px;font-weight:700;color:var(--gold)}

.testimonials{position:absolute;top:1580px;left:117px;width:470px}
.left-eyebrow{font-size:13px;color:var(--gold);text-transform:uppercase}
.left-title{font-size:31px;font-weight:700;color:var(--ink);line-height:34px;margin-top:2px}
.testimonials .quote{margin-top:24px;height:28px;display:block}
.testimonials .body{margin-top:16px;margin-left:5px;font-size:12.5px;line-height:15.5px;text-align:justify;color:#777;width:458px}
.testimonials .author{margin-top:15px;font-size:12.5px;color:var(--gold)}
.dots{display:flex;gap:5px;margin-top:20px;margin-left:4px}
.dots span{width:6px;height:6px;border-radius:50%;background:#aaa}
.dots span:first-child{background:var(--gold)}

.articles{position:absolute;top:1580px;left:648px;width:440px;height:290px}
.articles .left-eyebrow{margin-left:6px}
.article{position:absolute;left:0;width:440px}
.date{position:absolute;left:0;top:0;width:43px;height:55px;background:var(--gold)}
.date b{display:block;height:38px;line-height:40px;text-align:center;color:var(--white);font-size:23px;font-weight:400}
.date i{display:block;height:17px;line-height:17px;text-align:center;background:#111;color:var(--white);font-size:11px;font-style:normal}
.article h4{position:absolute;left:58px;top:0;font-size:14.5px;font-weight:700;color:var(--gold);white-space:nowrap}
.article p{position:absolute;left:58px;top:20px;width:380px;font-size:12.5px;line-height:16px;color:#666}
.btn-flat{position:absolute;left:2px;top:251px;width:107px;height:32px;line-height:32px;text-align:center;background:var(--gold-light);color:var(--white);font-size:14px}

/* footer */
.site-footer{position:absolute;top:1949px;left:0;width:1200px;height:296px;background:var(--footer);color:#ddd}
.foot-brand{left:113px;top:70px}
.foot-brand .brand-name{font-size:16px;color:#ccc}
.foot-brand .brand-dot{width:12px;height:12px}
.foot-about{left:110px;top:126px;width:270px;font-size:12.5px;line-height:15.3px;text-align:justify}
.foot-social{left:113px;top:217px;display:flex;gap:2px}
.foot-social span{width:23px;height:23px;background:var(--gold-light)}
.foot-head{font-size:14px;font-weight:700;color:var(--gold-light)}
.quick{left:457px;top:64px}
.quick ul{list-style:none;margin-top:18px}
.quick li{font-size:12.5px;height:23.5px;display:flex;align-items:flex-start;gap:12px}
.quick li::before{content:"";width:0;height:0;margin-top:4px;border-left:7px solid var(--gold-light);border-top:4px solid transparent;border-bottom:4px solid transparent}
.what{left:644px;top:64px}
.what ul{list-style:none;margin-top:17px;width:156px}
.what li{font-size:12.5px;height:25.6px;padding-top:2px;border-bottom:1px solid #ccc}
.what li:last-child{border-bottom:none}
.contact{left:870px;top:64px}
.contact-line{position:absolute;left:0;display:flex;gap:12px;font-size:12.5px;line-height:15px;white-space:nowrap}
.contact-line svg{flex:none;margin-top:1px}
.copyright{position:absolute;top:2245px;left:0;width:1200px;height:33px;background:var(--footer-bar);color:#ccc;font-size:12.5px;text-align:center;line-height:38px}
</style>
</head>
<body>

<header class="site-header">
  <a class="brand header-brand abs" href="#"><span class="brand-dot"></span><span class="brand-name">Summit Crest Advisors</span></a>
  <div class="contact-block call abs">
    <div class="label"><svg width="12" height="12" viewBox="0 0 24 24"><path fill="#c3902f" d="M6.6 10.8a15 15 0 0 0 6.6 6.6l2.2-2.2c.3-.3.7-.4 1-.2 1.1.4 2.3.6 3.6.6.6 0 1 .4 1 1V20c0 .6-.4 1-1 1A17 17 0 0 1 3 4c0-.6.4-1 1-1h3.5c.6 0 1 .4 1 1 0 1.3.2 2.5.6 3.6.1.3 0 .7-.2 1z"/></svg>Call Us Now</div>
    <div class="value">+ (555) 014-2286</div>
  </div>
  <div class="contact-block mail abs">
    <div class="label"><svg width="14" height="10" viewBox="0 0 14 10"><rect width="14" height="10" fill="#c3902f"/><path d="M0 0l7 5 7-5" stroke="#fff" fill="none"/></svg>Contact Email</div>
    <div class="value">info@summitcrestadvisors.com</div>
  </div>
  <div class="follow abs">
    <div class="label">Follow Us</div>
    <div class="social-row"><span></span><span></span><span></span><span></span><span></span></div>
  </div>
</header>

<nav class="main-nav">
  <a class="active" href="#" style="left:134px">Home</a>
  <a href="#" style="left:246px">About Us</a>
  <a href="#" style="left:372px">Services</a>
  <a href="#" style="left:500px">Our Team</a>
  <a href="#" style="left:639px">Blog</a>
  <a href="#" style="left:744px">Content</a>
  <a href="#" style="left:857px">Contact Us</a>
  <a class="appointment" href="#">Make Appointment</a>
</nav>

<section class="hero" role="img" aria-label="Photo of two business people shaking hands across an office desk">
  <h1>We help you Invest in technology professional services companies,</h1>
  <p>At cum veri epicurei constituto, legendos maluisset ne vis. Nam nulla incorrupte id. In labore&nbsp; suscipit salutandi vix. Ne odio persius omittam cum</p>
  <a class="btn" href="#">Contact us</a>
</section>

<section class="about">
  <div class="eyebrow">About Us</div>
  <h2 class="title">Welcome to Summit Crest Advisors</h2>
  <div class="copy">
    <p>Lorem ipsum dolor sit amet, cu per porro dolore nostro, partem integre corpora per ea, tation ornatus mel ad. Brute voluptatibus an est, per cu utroque torquatos, ei eum amet hinc. Ne vix ludus timeam definitionem. His hinc dicunt minimum cu, qui te dico laoreet. Sea ea mucius diceret solens, eos ei nostrud appellantur, an autem vocent novum doctus id mel. Id everti commune accusata melsunt explicabo. Nemo enim ipsam voluptatem quia voluptas sit aspernatur aut odit aut fugit,</p>
    <p>sed quia consequuntur magni dolores eos qui ratione voluptatem sequi nesciunt. Neque porro quisquam est, qui dolorem ipsum quia dolor sit amet, consectetur, adipisci velit, sed quia non numquam eius modi tempora incidunt ut labore et dolore magnam aliquam</p>
  </div>
  <a class="pill" href="#">READ MORE</a>
</section>

<section class="services">
  <div class="eyebrow">Viderer nostrud an est</div>
  <h2 class="title">Our Main Services</h2>
  <p class="intro">quo in errem diceret tincidunt. Usu te alii argumentum, vis ea platonem reprehendunt. Et liber nostrud temporibus mei, viderer nostrud an est. Splendide definitionem at pro. Ut sit putant legimus an viris scripta deterruisset sit. Ad movet labitur reprimique cum, no his qualisque consetetur.</p>

  <div class="service" style="left:164px">
    <svg viewBox="0 0 70 62" width="70"><circle cx="24" cy="24" r="8" fill="#c3902f"/><path d="M8 60V44c0-6 6-10 16-10s16 4 16 10v16z" fill="#c3902f"/><path d="M24 36l-2 4 2 14 2-14z" fill="#f4f3f3"/><circle cx="52" cy="16" r="12" fill="none" stroke="#c3902f" stroke-width="2.5"/><text x="52" y="22" font-size="16" font-family="Lato,sans-serif" font-weight="700" fill="#c3902f" text-anchor="middle">$</text></svg>
    <h3>Investment Services</h3>
    <p>Lorem ipsum dolor sit amet, consectetur adipiscing elit, sed do eiusmod tempor incididunt ut labore et</p>
    <a class="more" href="#">READ MORE</a>
  </div>
  <div class="service" style="left:462px">
    <svg viewBox="0 0 50 62" width="50"><path d="M3 3h34l10 10v46H3z" fill="none" stroke="#c3902f" stroke-width="3"/><rect x="12" y="20" width="8" height="8" fill="none" stroke="#c3902f" stroke-width="2"/><circle cx="34" cy="24" r="4" fill="none" stroke="#c3902f" stroke-width="2"/><circle cx="34" cy="44" r="4" fill="none" stroke="#c3902f" stroke-width="2"/><path d="M20 24h10M16 28v16h14M34 28v12" stroke="#c3902f" stroke-width="2" fill="none"/></svg>
    <h3>Financial Services</h3>
    <p>Lorem ipsum dolor sit amet, consectetur adipiscing elit, sed do eiusmod tempor incididunt ut labore et</p>
    <a class="more" href="#">READ MORE</a>
  </div>
  <div class="service" style="left:772px">
    <svg viewBox="0 0 80 56" width="80"><g fill="#c3902f"><rect x="2" y="6" width="26" height="7" rx="3"/><rect x="2" y="16" width="26" height="7" rx="3"/><rect x="2" y="26" width="26" height="7" rx="3"/><rect x="2" y="36" width="26" height="7" rx="3"/><rect x="2" y="46" width="26" height="7" rx="3"/><rect x="52" y="16" width="26" height="7" rx="3"/><rect x="52" y="26" width="26" height="7" rx="3"/><rect x="52" y="36" width="26" height="7" rx="3"/><rect x="52" y="46" width="26" height="7" rx="3"/></g><circle cx="40" cy="38" r="15" fill="#f4f3f3" stroke="#c3902f" stroke-width="3"/><text x="40" y="45" font-size="19" font-family="Lato,sans-serif" font-weight="700" fill="#c3902f" text-anchor="middle">$</text></svg>
    <h3>Customer Services</h3>
    <p>Lorem ipsum dolor sit amet, consectetur adipiscing elit, sed do eiusmod tempor incididunt ut labore et</p>
    <a class="more" href="#">READ MORE</a>
  </div>
</section>

<section class="testimonials">
  <div class="left-eyebrow">Testimonials</div>
  <h2 class="left-title">What Client Says</h2>
  <svg class="quote" width="32" height="28" viewBox="0 0 32 28"><path d="M2 28V14C2 6 6 2 13 1v5c-4 1-5 3-5 7h5v15zM19 28V14c0-8 4-12 11-13v5c-4 1-5 3-5 7h5v15z" fill="#c3902f"/></svg>
  <p class="body">Duo Reges: constructio interrete. Quia nec honesto quic quam honestius nec turpi turpius. Tria genera bonorum; Quid iudicant sensus? Quae qui non vident, nihil umquam magnum ac cognitione dignum amaverunt. Dicet pro me ipsa virtus nec dubitabit isti vestro beato M. Nihil ad rem! Ne sit sane; qui non vident, nihil umquam magnum ac cognitione dignum amaverunt. quam honestius nec turpi turpius. Tria genera bonorum</p>
  <div class="author">-Daniel</div>
  <div class="dots"><span></span><span></span><span></span></div>
</section>

<section class="articles">
  <div class="left-eyebrow">Ostrud an est</div>
  <h2 class="left-title">Articles</h2>
  <article class="article" style="top:82px">
    <div class="date"><b>05</b><i>JAN</i></div>
    <h4>Porro dolore nostro Lorem ipsum dolor sit ametcu per</h4>
    <p>Lorem ipsum dolor sit amet, cu per porro dolore nostro, partem integre corpora per ea, tation ornatus mel ad Brute</p>
  </article>
  <article class="article" style="top:163px">
    <div class="date"><b>03</b><i>JAN</i></div>
    <h4>Dlore nostro Lorem ipsum dolor sit ametcu per nostro</h4>
    <p>Lorem ipsum dolor sit amet, cu per porro dolore nostro, partem integre corpora per ea, tation ornatus mel ad Brute</p>
  </article>
  <a class="btn-flat" href="#">Read more</a>
</section>

<footer class="site-footer">
  <div class="foot-brand brand abs"><span class="brand-dot"></span><span class="brand-name">Summit Crest Advisors</span></div>
  <p class="foot-about abs">Lorem ipsum dolor sit amet, cu per porro dolore nostro, partem integre corpora per ea, tation ornatus mel ad. Brute voluptatibus an est, per cu utroque torquatos, ei eum amet hinc.</p>
  <div class="foot-social abs"><span></span><span></span><span></span><span></span><span></span></div>

  <div class="quick abs">
    <div class="foot-head">Quick Link</div>
    <ul><li>About us</li><li>Services</li><li>Our Team</li><li>Blog</li><li>Content</li><li>Contact us</li></ul>
  </div>
  <div class="what abs">
    <div class="foot-head">What We do</div>
    <ul><li>Epicurei constituto</li><li>Legendos maluisset</li><li>Usu te alii argumentum</li><li>Labitur reprimique</li><li>Dolorum adolescens</li><li>Discere antiopam</li></ul>
  </div>
  <div class="contact abs">
    <div class="foot-head">Contact info</div>
    <div class="contact-line" style="top:49px"><svg width="12" height="16" viewBox="0 0 12 16"><path d="M6 0a6 6 0 0 0-6 6c0 4.5 6 10 6 10s6-5.5 6-10a6 6 0 0 0-6-6z" fill="#d9ae45"/><circle cx="6" cy="6" r="2.2" fill="#1f1f1f"/></svg><span>Summit Crest Advisors<br>1480 Meridian Lane<br>Fairview, USA</span></div>
    <div class="contact-line" style="top:120px;font-weight:700"><svg width="13" height="13" viewBox="0 0 24 24"><path fill="#d9ae45" d="M6.6 10.8a15 15 0 0 0 6.6 6.6l2.2-2.2c.3-.3.7-.4 1-.2 1.1.4 2.3.6 3.6.6.6 0 1 .4 1 1V20c0 .6-.4 1-1 1A17 17 0 0 1 3 4c0-.6.4-1 1-1h3.5c.6 0 1 .4 1 1 0 1.3.2 2.5.6 3.6.1.3 0 .7-.2 1z"/></svg><span>+ (555) 014-2286</span></div>
    <div class="contact-line" style="top:149px"><svg width="13" height="10" viewBox="0 0 14 10"><rect width="14" height="10" fill="#d9ae45"/><path d="M0 0l7 5 7-5" stroke="#1f1f1f" fill="none"/></svg><span>info@summitcrestadvisors.com</span></div>
  </div>
</footer>
<div class="copyright">Copyright 2020, Summit Crest Advisors, All Right Reserved</div>

</body>
</html>
```